Consulting/ Manufacturers Representative Website

I need a website for a consulting/manufacturer representative company in Texas called Birchwell Venture Advisors. We Uncover and implement the right solution, at the right time, in the right way. We consult, we train, we offer project management, we offer performance improvement, we offer value creation, we turn stagnation into growth, and we offer corporate performance improvement.
I want the design to load on desktop and mobile, I want the site to look and feel professional like a large firm, and I want the site to be a marketing tool and establish a strong online presence.

Target Market(s)

City Governments, State Governments, County Governments, US Government, Power Plants, Refineries, Chemical Plants, Industrial customers

Industry/Entity Type

Consulting

Number of Pages Required

5+ page

Requirements
Must have
• mobile and desktop compatible, professional look, must be a fast website, company email and contact capabilities, contact page, company logo on website, SEO optimized, must display different industries served: Energy, Public (Government, Not For Profit, Educational), Transportation & Logistics, Business Services.
• Show that I help customers operate in a cleaner, safer and more economical way.
Nice to have
• news letter, news feed, show that company is principles based.
Should not have
• slow site, cheap look

```html
<!DOCTYPE html>
<html lang="en">
<head>
<meta charset="utf-8">
<title>Birchwell Venture Advisors</title>
<link rel="stylesheet" href="https://fonts.googleapis.com/css2?family=Montserrat:wght@400;500;600;700&family=Oswald:wght@400;500&display=swap">
<style>
:root{
  --blue:#1570ef;
  --blue-dark:#0d5fd6;
  --yellow:#f3e13c;
  --ink:#1d1d22;
  --grey:#8a8f98;
  --white:#ffffff;
  --field:rgba(255,255,255,.72);
}
*{box-sizing:border-box;margin:0;padding:0}
html,body{width:1200px;height:2908px;overflow:hidden}
body{position:relative;background:var(--white);font-family:"Montserrat",sans-serif;color:var(--ink)}
.abs{position:absolute}

/* header / hero */
.hero-photo{left:194px;top:0;width:1006px;height:527px;
  background:linear-gradient(180deg,#2e5fa8 0%,#5a86c2 35%,#8c7f78 62%,#3b3a44 82%,#232431 100%)}
.logo{left:110px;top:0;width:140px;height:140px;background:var(--blue);padding:48px 0 0 16px;color:var(--yellow);font-weight:600}
.logo .name{font-size:27px;letter-spacing:1px;line-height:1}
.logo .sub{font-size:11px;line-height:15px;margin-top:10px;text-transform:uppercase}
.call{left:962px;top:62px;color:var(--white);font-size:13px;font-weight:600}
.menu{left:1133px;top:61px}
.hero-title{left:279px;top:226px;color:var(--white);font-size:38px;font-weight:400}
.hero-sub{left:279px;top:272px;color:var(--white);font-size:22px;font-weight:400}
.hero-btn{left:279px;top:320px;width:149px;height:32px;border:1px solid rgba(255,255,255,.7);color:var(--white);font-size:11px;font-weight:600;text-align:center;line-height:30px;letter-spacing:1px}
.dot{width:6px;height:6px;border-radius:50%;background:#b9c2d2;left:137px}
.down{left:575px;top:502px}

/* side labels */
.side-label{left:25px;width:37px;border:1.5px solid var(--blue);background:var(--white)}
.side-label span{position:absolute;left:50%;top:50%;transform:translate(-50%,-50%) rotate(-90deg);white-space:nowrap;font-size:11px;font-weight:600;color:var(--blue);letter-spacing:.5px}

/* about */
.about-title{left:279px;top:630px;font-size:21px;font-weight:600;letter-spacing:.5px}
.about-sub{left:279px;top:660px;font-size:10px;font-weight:600;text-transform:uppercase}
.about-text{left:638px;top:630px;width:452px;font-size:13px;line-height:22px;color:var(--grey)}
.plus{width:20px;height:20px;background:var(--blue);color:var(--white);font-size:16px;line-height:20px;text-align:center;font-weight:600}

/* services */
.band{left:0;width:1200px;background:var(--blue)}
.photo{display:block}
.svc-title{color:var(--white);font-size:21px;font-weight:600;line-height:32px;text-transform:uppercase;letter-spacing:.5px}
.svc-text{color:var(--white);font-size:13px;line-height:21px}
.learn{display:flex;align-items:center;gap:12px;font-size:11px;font-weight:600;letter-spacing:.5px}
.learn.light{color:var(--white)}
.learn.dark{color:var(--blue)}

/* why */
.why-title{left:0;width:1200px;top:1618px;text-align:center;font-size:22px;font-weight:500;letter-spacing:1px}
.why-sub{left:320px;width:560px;top:1652px;text-align:center;font-size:13px;line-height:21px;color:var(--grey)}
.feature{width:260px;text-align:center;color:var(--blue);font-size:11px;font-weight:600;line-height:18px;text-transform:uppercase}
.feature svg{display:block;margin:0 auto 16px}

/* team */
.member{top:2026px;width:225px;height:264px}
.member .name{position:absolute;left:0;right:0;bottom:-8px;text-align:center;font-family:"Oswald",sans-serif;color:var(--white);font-size:22px;font-weight:500;text-transform:uppercase}
.member .role{position:absolute;left:0;right:0;bottom:-28px;text-align:center;font-family:"Oswald",sans-serif;color:var(--white);font-size:11px;text-transform:uppercase}

/* contact */
.contact-photo{left:0;top:2379px;width:1006px;height:529px;
  background:linear-gradient(110deg,#f4e7dc 0%,#e9d2c2 25%,#b7c4dd 50%,#4f6fb8 75%,#2a3f86 100%)}
.contact-title{left:109px;top:2444px;font-size:21px;font-weight:600;letter-spacing:.5px}
.field{left:109px;width:479px;background:var(--field);font-size:12px;color:#9a9ea6;padding:9px 18px}
.send{left:109px;top:2802px;width:104px;height:35px;background:var(--blue);color:var(--white);font-size:12px;font-weight:600;text-align:center;line-height:35px;letter-spacing:1px}
.social{left:1044px;width:33px;height:33px;border:1.5px solid var(--blue);display:flex;align-items:center;justify-content:center}
.social.on{background:var(--blue)}
.copyright{left:1025px;top:2770px;transform:rotate(-90deg);transform-origin:left top;font-size:9px;font-weight:600;color:var(--blue);line-height:13px;text-transform:uppercase;white-space:nowrap}
.up{left:1119px;top:2787px}
</style>
</head>
<body>

<!-- Header & hero -->
<div class="abs hero-photo" role="img" aria-label="Photo of a city skyline with office towers at dusk"></div>
<div class="abs logo"><div class="name">BIRCHWELL</div><div class="sub">Venture<br>Advisors</div></div>
<div class="abs call">Call: 555-0148-27</div>
<svg class="abs menu" width="22" height="16" viewBox="0 0 22 16"><rect y="0" width="22" height="2.5" fill="#fff"/><rect y="6.5" width="22" height="2.5" fill="#fff"/><rect y="13" width="22" height="2.5" fill="#fff"/></svg>
<div class="abs hero-title">We Uncover &amp; implement</div>
<div class="abs hero-sub">the right solution, at the right time, in the right way</div>
<div class="abs hero-btn">CONSULT NOW!</div>
<div class="abs dot" style="top:385px"></div>
<div class="abs dot" style="top:420px"></div>
<div class="abs dot" style="top:455px"></div>
<svg class="abs" style="left:130px;top:480px" width="20" height="20" viewBox="0 0 20 20"><rect x="4" y="4" width="12" height="12" transform="rotate(45 10 10)" fill="none" stroke="#1570ef" stroke-width="1.5"/><circle cx="10" cy="10" r="2.5" fill="#1570ef"/></svg>
<svg class="abs down" width="50" height="50" viewBox="0 0 50 50"><rect x="10" y="10" width="30" height="30" transform="rotate(45 25 25)" fill="#1570ef"/><path d="M25 19v12M21 27l4 4 4-4" stroke="#fff" stroke-width="1.8" fill="none"/></svg>

<!-- About -->
<div class="abs side-label" style="top:617px;height:159px"><span>ABOUT US</span></div>
<div class="abs about-title">WELCOME TO BIRCHWELL</div>
<div class="abs about-sub">Venture Advisors</div>
<p class="abs about-text">We are consulting/manufacturer representative company in dolor Lorem ipsum dolor sit amet, consectetur adipiscing elit, sed tempor incididunt ut labore et dolore magna aliqua. Ut enim ad minim veniam, quis nostrud exercitation ullamco laboris nisi ut aliquip ex ea commodo consequat. Duis aute irure dolor in reprehenderit in voluptate velit esse.</p>
<div class="abs plus" style="left:638px;top:781px">+</div>

<!-- Services -->
<div class="abs band" style="top:905px;height:611px"></div>
<div class="abs side-label" style="top:969px;height:156px"><span>SERVICES</span></div>
<div class="abs photo" style="left:110px;top:872px;width:478px;height:353px;background:linear-gradient(135deg,#eef0f2 0%,#cdd3da 45%,#4a4e58 80%,#2a2c33 100%)" role="img" aria-label="Photo of a trainer presenting at a whiteboard to a seated group"></div>
<div class="abs svc-title" style="left:640px;top:966px;width:420px">Consulting &amp; Training<br>Services</div>
<p class="abs svc-text" style="left:640px;top:1038px;width:450px">Lorem ipsum dolor sit amet, consectetur adipiscing elit, sed do eiusmod tempor incididunt ut labore et dolore magna aliqua. Ut enim ad minim veniam, quis nostrud exercitation ullamco laboris nisi ut aliquip ex ea commodo consequat.</p>
<div class="abs learn light" style="left:636px;top:1156px"><svg width="30" height="30" viewBox="0 0 30 30"><rect x="6" y="6" width="18" height="18" transform="rotate(45 15 15)" fill="#fff"/><path d="M15 11v8M11 15h8" stroke="#1570ef" stroke-width="1.6"/></svg>LEARN MORE</div>

<div class="abs svc-title" style="left:109px;top:1268px;width:420px">Project Management<br>Service</div>
<p class="abs svc-text" style="left:109px;top:1338px;width:450px">Lorem ipsum dolor sit amet, consectetur adipiscing elit, sed doeiusmod tempor incididunt ut labore et dolore magna aliqua. Ut enim ad minim veniam, quis nostrud exercitation ullamco laboris nisi ut aliquip ex ea commodo consequat.</p>
<div class="abs plus" style="left:109px;top:1454px;background:#fff;color:var(--blue)">+</div>
<div class="abs photo" style="left:613px;top:1253px;width:477px;height:298px;background:linear-gradient(120deg,#c9d2d8 0%,#8d969e 40%,#4b4f55 70%,#d9dde0 100%)" role="img" aria-label="Photo of colleagues in a meeting around a glass table"></div>

<!-- Why -->
<div class="abs side-label" style="top:1615px;height:155px"><span>WE OFFER</span></div>
<div class="abs why-title">WHY BIRCHWELL</div>
<p class="abs why-sub">Lorem ipsum dolor sit amet, consectetur adipiscing elit, sed do eiusmod tempor incididunt ut labore et dolore magna aliqua.</p>
<div class="abs feature" style="left:134px;top:1728px">
  <svg width="60" height="48" viewBox="0 0 60 48" fill="none" stroke="#1570ef" stroke-width="2"><circle cx="30" cy="7" r="4"/><path d="M24 18a6 6 0 0 1 12 0"/><path d="M30 20v6M14 26h32M14 26v6M46 26v6"/><circle cx="14" cy="35" r="3.5"/><circle cx="46" cy="35" r="3.5"/><circle cx="30" cy="35" r="3.5"/><path d="M8 46a6 6 0 0 1 12 0M24 46a6 6 0 0 1 12 0M40 46a6 6 0 0 1 12 0"/></svg>
  Corporate Performance<br>Improvement</div>
<div class="abs feature" style="left:470px;top:1728px">
  <svg width="60" height="48" viewBox="0 0 60 48" fill="none" stroke="#1570ef" stroke-width="2"><path d="M22 4h16v8l-3 3v15l4 4v5H21v-5l4-4V15l-3-3z"/><path d="M27 4v4M33 4v4M18 45h24"/></svg>
  Strategy and Value<br>Creation</div>
<div class="abs feature" style="left:805px;top:1728px">
  <svg width="64" height="48" viewBox="0 0 64 48" fill="none" stroke="#1570ef" stroke-width="2"><path d="M6 46V24a4 4 0 0 1 8 0v22M18 46V16a4 4 0 0 1 8 0v30M30 46V12a4 4 0 0 1 8 0v34M42 46V8a4 4 0 0 1 8 0v38M2 46h58"/></svg>
  We turn stagnation into<br>growth</div>
<div class="abs learn dark" style="left:583px;top:1857px"><svg width="30" height="30" viewBox="0 0 30 30"><rect x="6" y="6" width="18" height="18" transform="rotate(45 15 15)" fill="#1570ef"/><path d="M15 11v8M11 15h8" stroke="#fff" stroke-width="1.6"/></svg>LEARN MORE</div>

<!-- Team -->
<div class="abs band" style="top:1955px;height:424px"></div>
<div class="abs side-label" style="top:2016px;height:156px"><span>OUR TEAM</span></div>
<div class="abs member" style="left:110px;background:linear-gradient(180deg,#d8d8d8 0%,#a8a8a8 55%,#222 100%)" role="img" aria-label="Portrait photo of team member"><div class="name">Daniel Morrow</div><div class="role">Business Operator</div></div>
<div class="abs member" style="left:362px;background:linear-gradient(180deg,#cfcfcf 0%,#8c8c8c 55%,#1d1d1d 100%)" role="img" aria-label="Portrait photo of team member"><div class="name">Clara Whitfield</div><div class="role">Consultant</div></div>
<div class="abs member" style="left:613px;background:linear-gradient(180deg,#dcdcdc 0%,#a3a3a3 55%,#262626 100%)" role="img" aria-label="Portrait photo of team member"><div class="name">Owen Hartley</div><div class="role">Advisor</div></div>
<div class="abs member" style="left:865px;background:linear-gradient(180deg,#d4d4d4 0%,#8e8e8e 55%,#1b1b1b 100%)" role="img" aria-label="Portrait photo of team member"><div class="name">Marcus Bell</div><div class="role">Business Operator</div></div>

<!-- Contact -->
<div class="abs contact-photo" role="img" aria-label="Photo looking up at a glass office building"></div>
<div class="abs side-label" style="top:2438px;height:156px"><span>CONTACT US</span></div>
<div class="abs contact-title">GET IN TOUCH WITH US</div>
<div class="abs field" style="top:2492px;height:34px">Your Name</div>
<div class="abs field" style="top:2540px;height:35px">Email</div>
<div class="abs field" style="top:2589px;height:33px">Phone</div>
<div class="abs field" style="top:2637px;height:140px">Type your message</div>
<div class="abs send">SEND</div>

<div class="abs social" style="top:2450px"><svg width="8" height="8"><rect width="8" height="8" fill="#1570ef"/></svg></div>
<div class="abs social on" style="top:2495px"><svg width="8" height="8"><rect width="8" height="8" fill="#fff"/></svg></div>
<div class="abs social" style="top:2540px"><svg width="8" height="8"><rect width="8" height="8" fill="#1570ef"/></svg></div>
<div class="abs social" style="top:2584px"><svg width="8" height="8"><rect width="8" height="8" fill="#1570ef"/></svg></div>
<div class="abs copyright">©2018 Birchwell<br>Venture Advisors.</div>
<svg class="abs up" width="50" height="50" viewBox="0 0 50 50"><rect x="10" y="10" width="30" height="30" transform="rotate(45 25 25)" fill="#1570ef"/><path d="M25 31V19M21 23l4-4 4 4" stroke="#fff" stroke-width="1.8" fill="none"/></svg>

</body>
</html>
```